Letterhead design for ZENTORA company

I need an A4 letterhead design for my company "Zentora Electrical Products". I need the letterhead to match my current logo and business card designs. I would like it to be colourful and match the design of the business card in terms of the flowing line of colour where the information is.  

Target Market(s)

Adults aged 20 - 50 Upper middle class.

Industry/Entity Type

It Company

Requirements
Must have
• Must be A4 size and match my current logo and business card designs. Must be clean simple and eye catching.

• Must have the following information

• Zentora Electrical Products LTD
• 7 Ardley Close
• Chiswick
• London
• England
• W9 3QX
• Company No. 05316429
• VAT No. GB 627150384

• Telephone: 02081594360
• Mobile: 07815062247
• Email: info@zentora-goods.co.uk
Nice to have
• nice to have a wave of colour like the business card.
Should not have
• Should not be a different colour scheme to the business card and logo design.

```html
<!DOCTYPE html>
<html lang="en">
<head>
<meta charset="utf-8">
<title>Zentora Electrical Products – Letterhead</title>
<link rel="stylesheet" href="https://fonts.googleapis.com/css2?family=Carlito:wght@400&display=swap">
<style>
  :root {
    --paper: #ffffff;
    --teal-deep: #007592;
    --teal: #0a9bbd;
    --cyan: #4fc8e8;
    --sky: #8dd5f3;
    --mist-light: #fbfbfb;
    --mist: #dedfe1;
    --brand: #1583ab;
    --ink: #2b2b2b;
  }
  html, body {
    margin: 0;
    padding: 0;
    width: 874px;
    height: 1200px;
    overflow: hidden;
    background: var(--paper);
  }
  .letterhead {
    position: relative;
    width: 874px;
    height: 1200px;
    background: var(--paper);
    font-family: "Carlito", "Calibri", sans-serif;
    color: var(--ink);
  }
  .waves {
    position: absolute;
    inset: 0;
    width: 874px;
    height: 1200px;
  }
  .brand {
    position: absolute;
    top: 28px;
    right: 26px;
    text-align: right;
    color: var(--brand);
    font-weight: 400;
    line-height: 1;
  }
  .brand-name {
    display: block;
    font-size: 66px;
    letter-spacing: 3px;
  }
  .brand-line {
    display: block;
    margin-top: 4px;
    font-size: 25px;
    letter-spacing: 2px;
  }
  .footer-text {
    position: absolute;
    font-size: 14px;
    line-height: 17px;
    margin: 0;
  }
  .address { left: 29px; top: 1054px; font-style: normal; }
  .company-no { left: 29px; top: 1139px; }
  .vat-no { left: 240px; top: 1139px; }
  .contact { right: 31px; top: 1105px; text-align: right; }
</style>
</head>
<body>
<main class="letterhead">
  <svg class="waves" viewBox="80 84 1492 2104" preserveAspectRatio="none" aria-hidden="true">
    <defs>
      <linearGradient id="band" x1="0" y1="0" x2="1" y2="0">
        <stop offset="0" stop-color="var(--teal-deep)"/>
        <stop offset="0.35" stop-color="var(--teal)"/>
        <stop offset="0.6" stop-color="var(--cyan)"/>
        <stop offset="0.8" stop-color="var(--teal)"/>
        <stop offset="1" stop-color="var(--teal-deep)"/>
      </linearGradient>
      <radialGradient id="mist-top" cx="0.35" cy="0.35" r="0.8">
        <stop offset="0" stop-color="var(--mist-light)"/>
        <stop offset="1" stop-color="var(--mist)"/>
      </radialGradient>
      <radialGradient id="mist-bottom" cx="0.6" cy="0.7" r="0.8">
        <stop offset="0" stop-color="var(--mist-light)"/>
        <stop offset="1" stop-color="var(--mist)"/>
      </radialGradient>
    </defs>

    <g class="wave-top">
      <path fill="var(--teal-deep)" d="M595,84 C780,320 1100,440 1390,440 C1470,440 1530,430 1572,418 L1572,84 Z"/>
      <path fill="url(#band)" d="M640,84 C840,300 1150,410 1390,408 C1470,408 1530,398 1572,388 L1572,84 Z"/>
      <path fill="var(--sky)" d="M678,84 C878,290 1180,372 1400,370 C1480,370 1530,360 1572,350 L1572,84 Z"/>
      <path fill="url(#mist-top)" d="M700,84 C900,282 1190,366 1400,365 C1480,365 1530,357 1572,346 L1572,84 Z"/>
    </g>

    <g class="wave-bottom">
      <path fill="var(--teal-deep)" d="M80,1806 C140,1793 200,1788 265,1788 C620,1788 960,1960 1185,2188 L80,2188 Z"/>
      <path fill="url(#band)" d="M80,1840 C140,1830 200,1826 265,1826 C600,1826 930,1975 1150,2188 L80,2188 Z"/>
      <path fill="var(--sky)" d="M80,1888 C150,1878 210,1874 265,1874 C585,1874 900,2005 1110,2188 L80,2188 Z"/>
      <path fill="url(#mist-bottom)" d="M80,1892 C150,1882 210,1878 265,1878 C580,1878 880,2012 1085,2188 L80,2188 Z"/>
    </g>
  </svg>

  <header class="brand">
    <span class="brand-name">ZENTORA</span>
    <span class="brand-line">Electrical Products</span>
  </header>

  <address class="footer-text address">
    Zentora Electrical Products LTD<br>
    7 Ardley Close, Chiswick<br>
    London W9 3QX<br>
    England
  </address>
  <p class="footer-text company-no">Company No. 05316429</p>
  <p class="footer-text vat-no">VAT No. GB 627150384</p>
  <p class="footer-text contact">
    Telephone: 02081594360<br>
    Mobile: 07815062247<br>
    Email: info@zentora-goods.co.uk
  </p>
</main>
</body>
</html>
```